plovu business card design

plovu is an incubator within RTM Media focused on unlocking the potential in underserved niche micro-verticals on the web. our mission is to rapidly develop and foster emerging micro-verticals bc they are ripe for growth - building interesting and trusted content experiences with unqiue, useful and cutting-edge delivery methods.please do all copy (except for RTM Media, which must look as typed here and in logo) in all lowercase. Also please use spaces between phone # extensions not dashes or periods. I have attached all variations of the logo.
Industry/Entity Type
Business
Contact Information for Business Card
daria feltow, ceo www.plovu.io 218 holbrook lane 3rd floor oakland ca 94731 415 602 0002m 510 985 7966d daria.feltow@plovu.io
Look and feel
Each slider illustrates characteristics of the customer's brand and the style your logo design should communicate.

```html
<!DOCTYPE html>
<html lang="en">
<head>
<meta charset="utf-8">
<title>plovu business card</title>
<link href="https://fonts.googleapis.com/css2?family=Hind:wght@400;500;600&display=swap" rel="stylesheet">
<style>
  :root {
    --backdrop: #a9a7a8;
    --ink: #17191c;
    --paper: #ffffff;
    --teal: #1a7b80;
    --text-dark: #1d1f22;
    --text-light: #ffffff;
  }
  * { margin: 0; padding: 0; box-sizing: border-box; }
  html, body {
    width: 1200px; height: 1200px; overflow: hidden;
    background: var(--backdrop);
    font-family: "Hind", Arial, sans-serif;
  }
  .canvas { position: relative; width: 1200px; height: 1200px; }

  .card {
    position: absolute;
    border-radius: 22px;
    overflow: hidden;
  }
  .card--front {
    left: 238px; top: 117px; width: 714px; height: 420px;
    background: var(--ink);
  }
  .card--back {
    left: 230px; top: 643px; width: 712px; height: 417px;
    background: var(--paper);
  }
  .card__art { position: absolute; inset: 0; width: 100%; height: 100%; }

  .brand { position: absolute; color: var(--text-light); }
  .brand__name {
    display: flex; align-items: center; gap: 14px;
    font-weight: 600; font-size: 128px; line-height: 1; letter-spacing: -1px;
  }
  .brand__dot {
    width: 26px; height: 26px; border-radius: 50%;
    background: var(--teal); margin-top: 30px;
  }
  .brand__tagline { font-weight: 500; font-size: 21px; margin-top: 2px; padding-left: 3px; }

  .card--front .brand { left: 207px; top: 125px; }
  .card--back .brand { left: 50px; top: 98px; color: var(--text-dark); }

  .holder {
    position: absolute; right: 36px; top: 52px;
    text-align: right; color: var(--text-light);
  }
  .holder__name { font-weight: 500; font-size: 26px; letter-spacing: 0.5px; line-height: 1.1; }
  .holder__role { font-size: 16px; margin-top: 4px; }

  .contacts {
    position: absolute; left: 48px; top: 288px;
    list-style: none; color: var(--text-dark); font-size: 18px;
  }
  .contacts li { display: flex; align-items: center; gap: 20px; height: 23.5px; }
  .contacts svg { width: 16px; height: 16px; fill: var(--teal); flex: none; }
  .contacts .accent { color: var(--teal); }

  .address {
    position: absolute; right: 45px; bottom: 36px;
    font-size: 18px; color: var(--text-dark);
  }
</style>
</head>
<body>
<main class="canvas">

  <section class="card card--front">
    <div class="brand">
      <div class="brand__name">plovu<span class="brand__dot"></span></div>
      <div class="brand__tagline">an RTM Media incubator</div>
    </div>
  </section>

  <section class="card card--back">
    <svg class="card__art" viewBox="0 0 712 417" preserveAspectRatio="none">
      <path fill="var(--teal)" d="M0,40 C150,5 330,-5 460,50 C560,95 620,170 712,178 L712,195 C610,192 540,125 430,78 C320,38 150,32 0,75 Z"/>
      <path fill="var(--paper)" d="M60,55 C200,25 330,30 430,68 C330,45 200,42 60,55 Z"/>
      <path fill="var(--ink)" d="M330,0 C470,12 575,140 712,172 L712,0 Z"/>
    </svg>

    <div class="brand">
      <div class="brand__name">plovu<span class="brand__dot"></span></div>
      <div class="brand__tagline">an RTM Media incubator</div>
    </div>

    <div class="holder">
      <div class="holder__name">Daria Feltow</div>
      <div class="holder__role">CEO</div>
    </div>

    <ul class="contacts">
      <li>
        <svg viewBox="0 0 16 16"><path d="M1 6c0-2 3-3 7-3s7 1 7 3l-3 1-1-2H5L4 7 1 6zm3 2h8l2 5H2l2-5z"/></svg>
        94731 415 738 4196m
      </li>
      <li>
        <svg viewBox="0 0 16 16"><path d="M4 1h8v14H4zM5.5 3v9h5V3z"/></svg>
        510 247 3859d
      </li>
      <li>
        <svg viewBox="0 0 16 16"><path d="M1 3h14v10H1zm1.5 1.5L8 9l5.5-4.5z"/></svg>
        daria.feltow@plovu.io
      </li>
      <li>
        <svg viewBox="0 0 16 16"><circle cx="8" cy="8" r="6.5"/></svg>
        <span>www.<span class="accent">plovu</span>.io</span>
      </li>
    </ul>

    <div class="address">218 holbrook lane 3rd floor oakland ca</div>
  </section>

</main>
</body>
</html>
```